Medical Herbalist needs labels for healing skin salves

I am bringing out a Calendula Salve and a Comfrey and Meadowsweet Salve, both have healing qualities and have have a history of Traditional use. I would like the label to look eye-cathching and colourful, orange based for Calendula and Green based for Comfrey. I particularly like Verbelle's image and their font. (skin care range - please look at this) I want to convey a sense of the Apothecary (most important) and slightly retro, old fashioned, quality about these salves.
I would like a design to fit on a label that goes around a 30ml or 60ml jar - I will be using both. I feel that the usp is that I am a Medical Herbalist producing hand made, containing natural ingredients - quality items made in Wales. (part of the UK) I have considered calling them Hearth Balms but not definite about this yet.
Measurements:
60ml jar - 31mm (height) x 150 to 160mm width - i.e. around the jar
30ml jar 18mm (height) x 105mm to 125mm width - i.e. around the jar

Reason: I would like to see some more designs before I make my decisions - I have not had enough that I am excited about so far I am afraid.

Target Market(s)

Adults, male and female but female bias. Wanting to solve problem i.e. dry chapped skin, cracked heals (Calendula). Sprains, aches and pains (Comfrey and Meadowsweet)

Industry/Entity Type

Medical

Font styles to use
Serif
Decorative

Colors
acd036
cadf82
e9f1ce
f79020
fece3e
faa54b

Requirements
Must have
• The kind of font and look I have suggested. Clearly Calendula Salve in large writing
and the same for the Comfrey and Meadowsweet Salve. It needs to have some impact
I need to have room to list ingredients.
Nice to have
• Possible images of the plants or part of the plants listed. I was not intending the photographs to be used - they were more to inspire hopefully.
Picture of pestle and mortar?
Should not have
• Anything too jokey or gimmicky.

```html
<!DOCTYPE html>
<html lang="en">
<head>
<meta charset="utf-8">
<title>Herbal Salve Labels</title>
<link rel="stylesheet" href="https://fonts.googleapis.com/css2?family=Sorts+Mill+Goudy:ital@0;1&display=swap">
<style>
:root{
  --frame:#d8c9a7;
  --frame-dark:#d3c29d;
  --badge:#c2ae86;
  --panel:#e9e0c9;
  --cream:#fbf7ea;
  --ink:#5b4a36;
  --orange:#f7901e;
  --orange-soft:#fbc98a;
  --green:#9ccc3c;
  --green-soft:#d7ebaa;
}
*{margin:0;padding:0;box-sizing:border-box}
html,body{width:1200px;height:693px;overflow:hidden;background:#fff}
body{position:relative;font-family:"Sorts Mill Goudy",Georgia,serif;color:var(--ink);font-variant-numeric:lining-nums}
.label{position:absolute;left:0;width:1200px;height:315px}
.label--calendula{top:0;--accent:var(--orange)}
.label--comfrey{top:378px;--accent:var(--green)}
.label-art{position:absolute;inset:0}
.maker-name{position:absolute;left:37px;top:72px;width:245px;height:88px;background:var(--panel);
  font-variant:small-caps;font-size:38px;line-height:34px;text-align:center;padding-top:10px;letter-spacing:1px}
.maker-role{position:absolute;left:37px;top:170px;width:245px;text-align:center;font-variant:small-caps;font-size:20px;letter-spacing:.5px}
.maker-address{position:absolute;left:20px;top:205px;width:280px;text-align:center;font-variant:small-caps;font-size:16px;line-height:25px}
.plant-art{position:absolute;border-radius:45%}
.product-title{position:absolute;left:445px;top:105px;width:310px;text-align:center;font-weight:normal;font-style:italic;font-size:46px;line-height:54px}
.label--comfrey .product-title{top:90px;font-size:38px;line-height:48px}
.volume{position:absolute;left:800px;top:262px;font-size:14px}
.ingredients{position:absolute;left:938px;top:40px;width:228px;height:188px;background:var(--panel);text-align:center;padding-top:6px}
.ingredients h2{font-weight:normal;font-variant:small-caps;font-size:18px;margin-bottom:5px}
.ingredients li{list-style:none;font-size:14px;line-height:19px}
.ingredients .rule{width:150px;height:1px;background:var(--ink);opacity:.4;margin:8px auto 7px}
.ingredients .use{font-style:italic;font-size:11px;line-height:16px;padding:0 8px}
.label--comfrey .ingredients{height:188px;padding-top:4px}
.label--comfrey .ingredients h2{margin-bottom:3px}
.label--comfrey .ingredients li{line-height:18.5px}
.label--comfrey .ingredients .rule{margin:5px auto 4px}
.label--comfrey .ingredients .use{line-height:15px;padding:0 14px}
.batch{position:absolute;left:978px;top:238px;width:188px;height:34px;border:2px solid var(--accent);
  color:var(--accent);font-size:9px;padding:5px 10px;letter-spacing:.5px}
.jar-icon{position:absolute;left:938px;top:238px;width:34px;height:34px;border:2px solid var(--accent);border-radius:50%}
.jar-icon::after{content:"";position:absolute;left:9px;top:8px;width:12px;height:14px;border:2px solid var(--accent);border-radius:2px}
</style>
</head>
<body>

<section class="label label--calendula">
  <svg class="label-art" viewBox="0 0 1200 315" aria-hidden="true">
    <defs>
      <pattern id="stripes-a" width="10" height="9" patternUnits="userSpaceOnUse">
        <rect width="10" height="9" fill="#fbf7ea"/><rect y="8" width="10" height="1" fill="#efe5cc"/>
      </pattern>
    </defs>
    <rect x="0" y="0" width="1200" height="315" fill="var(--frame)"/>
    <rect x="8" y="10" width="1184" height="295" fill="var(--orange)"/>
    <rect x="17" y="18" width="1166" height="279" fill="none" stroke="#fff" stroke-width="2" stroke-dasharray="2 4"/>
    <rect x="26" y="27" width="1148" height="261" fill="url(#stripes-a)"/>
    <rect x="545" y="0" width="110" height="315" fill="var(--frame-dark)"/>
    <ellipse cx="600" cy="170" rx="163" ry="130" fill="var(--frame)"/>
    <ellipse cx="600" cy="170" rx="140" ry="112" fill="var(--cream)"/>
    <ellipse cx="600" cy="170" rx="130" ry="103" fill="none" stroke="var(--frame-dark)" stroke-width="1.5"/>
    <circle cx="600" cy="58" r="22" fill="var(--badge)"/>
  </svg>
  <div class="maker-name">Eleanor<br>Pritchard</div>
  <div class="maker-role">Medical Herbalist</div>
  <div class="maker-address">Nant, Coedfelin, Llanwenog,<br>Ceredigion, Wales SA40 9QX.</div>
  <div class="plant-art" role="img" aria-label="Illustration of calendula flowers and leaves" style="left:285px;top:45px;width:160px;height:250px;background:radial-gradient(ellipse at center,#fbc98a 0%,#fde2bf 60%,rgba(251,247,234,0) 75%)"></div>
  <div class="plant-art" role="img" aria-label="Illustration of calendula flowers and leaves" style="left:740px;top:45px;width:180px;height:250px;background:radial-gradient(ellipse at center,#fbc98a 0%,#fde2bf 60%,rgba(251,247,234,0) 75%)"></div>
  <h1 class="product-title">Calendula<br>Salve</h1>
  <div class="volume">e 30ml. (1 fl. oz.)</div>
  <div class="ingredients">
    <h2>Ingredients</h2>
    <ul>
      <li>Prunus amygdalus dulcis oil</li>
      <li>Theobroma cacao seed butter</li>
      <li>Calendula officinalis extract</li>
      <li>Commiphora Myrrha oil</li>
      <li>Cera alba</li>
    </ul>
    <div class="rule"></div>
    <p class="use">Traditionally used for minor cuts, grazes<br>and dry chapped skin</p>
  </div>
  <div class="jar-icon"></div>
  <div class="batch">BATCH NO.</div>
</section>

<section class="label label--comfrey">
  <svg class="label-art" viewBox="0 0 1200 315" aria-hidden="true">
    <defs>
      <pattern id="stripes-b" width="10" height="9" patternUnits="userSpaceOnUse">
        <rect width="10" height="9" fill="#fbf7ea"/><rect y="8" width="10" height="1" fill="#efe5cc"/>
      </pattern>
    </defs>
    <rect x="0" y="0" width="1200" height="315" fill="var(--frame)"/>
    <rect x="8" y="10" width="1184" height="295" fill="var(--green)"/>
    <rect x="17" y="18" width="1166" height="279" fill="none" stroke="#fff" stroke-width="2" stroke-dasharray="2 4"/>
    <rect x="26" y="27" width="1148" height="261" fill="url(#stripes-b)"/>
    <rect x="545" y="0" width="110" height="315" fill="var(--frame-dark)"/>
    <ellipse cx="600" cy="170" rx="163" ry="130" fill="var(--frame)"/>
    <ellipse cx="600" cy="170" rx="140" ry="112" fill="var(--cream)"/>
    <ellipse cx="600" cy="170" rx="130" ry="103" fill="none" stroke="var(--frame-dark)" stroke-width="1.5"/>
    <circle cx="600" cy="58" r="22" fill="var(--badge)"/>
  </svg>
  <div class="maker-name">Eleanor<br>Pritchard</div>
  <div class="maker-role">Medical Herbalist</div>
  <div class="maker-address">Nant, Coedfelin, Llanwenog,<br>Ceredigion, Wales SA40 9QX.</div>
  <div class="plant-art" role="img" aria-label="Illustration of meadowsweet blossom clusters and leaves" style="left:285px;top:70px;width:170px;height:200px;background:radial-gradient(ellipse at center,#e7eec6 0%,#f1f4dc 60%,rgba(251,247,234,0) 75%)"></div>
  <div class="plant-art" role="img" aria-label="Illustration of comfrey stem with leaves and flowers" style="left:740px;top:45px;width:200px;height:235px;background:radial-gradient(ellipse at center,#b9dc70 0%,#dcedb0 60%,rgba(251,247,234,0) 75%)"></div>
  <h1 class="product-title">Comfrey &amp;<br>Meadowsweet<br>Salve</h1>
  <div class="volume">e 30ml. (1 fl. oz.)</div>
  <div class="ingredients">
    <h2>Ingredients</h2>
    <ul>
      <li>Olea Europaea Fruit Oil</li>
      <li>Theobroma cacao seed butter</li>
      <li>Cera alba</li>
      <li>Symphytum officinale leaf extract</li>
      <li>Spiraea Ulmaria extract</li>
      <li>Rosmarinus officinalis oil</li>
    </ul>
    <div class="rule"></div>
    <p class="use">Traditionally used to relieve<br>muscular aches, strains and sprains</p>
  </div>
  <div class="jar-icon"></div>
  <div class="batch">BATCH NO.</div>
</section>

</body>
</html>
```